Business Cards

Need a neat design for a new business card

Industry/Entity Type

Residential Construction

Contact Information for Business Card

Company Name- KOVE Construction Inc.
Owner- Marcus Tolliver
Phone number- (555)203-7481
Email- kovecohomes@brindlemail.example
Facebook- www.socialpage.example/kovecohomes

Colors
fefdec

```html
<!DOCTYPE html>
<html lang="en">
<head>
<meta charset="utf-8">
<title>KOVE Construction — Business Cards</title>
<link rel="stylesheet" href="https://fonts.googleapis.com/css2?family=Montserrat:ital,wght@0,400;0,500;0,700;1,400&display=swap">
<style>
  :root {
    --backdrop: #d9d7cf;
    --card: #fefdec;
    --ink: #1f1e1b;
    --ink-soft: #4a4842;
    --rule: #6b6860;
  }
  * { margin: 0; padding: 0; box-sizing: border-box; }
  html, body {
    width: 1200px;
    height: 1008px;
    overflow: hidden;
    background: var(--backdrop);
    font-family: "Montserrat", sans-serif;
    color: var(--ink);
  }
  .sheet {
    width: 1200px;
    height: 1008px;
    display: flex;
    flex-direction: column;
    align-items: center;
    justify-content: center;
    gap: 72px;
  }
  .card {
    width: 700px;
    height: 400px;
    background: var(--card);
    position: relative;
    box-shadow: 0 2px 6px rgba(0,0,0,0.12);
  }

  /* Front */
  .card-front {
    display: flex;
    align-items: center;
    justify-content: center;
    gap: 28px;
  }
  .front-mark {
    display: flex;
    align-items: center;
    gap: 12px;
  }
  .mark-square {
    width: 18px;
    height: 18px;
    background: var(--ink);
  }
  .mark-name {
    font-size: 34px;
    font-weight: 500;
    letter-spacing: 2px;
    color: var(--ink);
  }
  .front-divider {
    width: 1.5px;
    height: 96px;
    background: var(--rule);
  }
  .front-wordmark {
    display: flex;
    flex-direction: column;
    color: var(--ink);
    font-weight: 500;
  }
  .wordmark-name {
    font-size: 60px;
    letter-spacing: 4px;
    line-height: 1;
  }
  .wordmark-sub {
    font-size: 17px;
    letter-spacing: 3.5px;
    margin-top: 6px;
  }

  /* Back */
  .back-mark {
    position: absolute;
    left: 56px;
    top: 56px;
    display: flex;
    align-items: center;
    gap: 12px;
  }
  .back-mark .mark-name { font-size: 30px; }
  .back-mark .mark-sub {
    font-size: 13px;
    letter-spacing: 2.5px;
    font-weight: 500;
    display: block;
    margin-top: 2px;
  }
  .contact {
    position: absolute;
    left: 330px;
    top: 178px;
  }
  .contact-name {
    font-size: 22px;
    font-weight: 700;
  }
  .contact-role {
    font-size: 14px;
    font-style: italic;
    color: var(--ink-soft);
    margin: 2px 0 16px;
  }
  .contact-list { list-style: none; }
  .contact-list li {
    display: flex;
    align-items: center;
    gap: 10px;
    font-size: 14px;
    line-height: 1;
    margin-bottom: 9px;
    white-space: nowrap;
  }
  .contact-icon {
    width: 13px;
    height: 13px;
    flex: none;
  }
  .icon-square {
    width: 12px;
    height: 12px;
    background: var(--ink);
    flex: none;
  }
</style>
</head>
<body>
<main class="sheet">
  <section class="card card-front" aria-label="Business card front">
    <div class="front-mark">
      <span class="mark-square"></span>
      <span class="mark-name">KOVE</span>
    </div>
    <span class="front-divider"></span>
    <div class="front-wordmark">
      <span class="wordmark-name">KOVE</span>
      <span class="wordmark-sub">CONSTRUCTION</span>
    </div>
  </section>

  <section class="card card-back" aria-label="Business card back">
    <div class="back-mark">
      <span class="mark-square"></span>
      <div>
        <span class="mark-name">KOVE</span>
        <span class="mark-sub">CONSTRUCTION</span>
      </div>
    </div>
    <div class="contact">
      <p class="contact-name">Marcus Tolliver</p>
      <p class="contact-role">Owner</p>
      <ul class="contact-list">
        <li>
          <svg class="contact-icon" viewBox="0 0 24 24" aria-hidden="true"><path fill="currentColor" d="M6.6 10.8a15.1 15.1 0 0 0 6.6 6.6l2.2-2.2c.3-.3.7-.4 1-.2 1.1.4 2.3.6 3.6.6.6 0 1 .4 1 1V20c0 .6-.4 1-1 1A17 17 0 0 1 3 4c0-.6.4-1 1-1h3.5c.6 0 1 .4 1 1 0 1.3.2 2.5.6 3.6.1.3 0 .7-.2 1z"/></svg>
          <span>(555)203-7481</span>
        </li>
        <li>
          <svg class="contact-icon" viewBox="0 0 24 24" aria-hidden="true"><rect x="2" y="5" width="20" height="14" rx="1" fill="currentColor"/><path d="M3 6l9 7 9-7" fill="none" stroke="#fefdec" stroke-width="1.8"/></svg>
          <span>kovecohomes@brindlemail.example</span>
        </li>
        <li>
          <span class="icon-square"></span>
          <span>www.socialpage.example/kovecohomes</span>
        </li>
      </ul>
    </div>
  </section>
</main>
</body>
</html>
```